Australian Web Design company needs a business card design

We need a business card design for a Sydney based Web Design/Development company called "Tall Pine Web Design". We design, build and deploy websites for small to medium sized businesses. The final design should be clean and communicate that we are a professional and supportive company.
I'd like the Icon to be abstract. Something that embodies the power of the internet, needs to be clean/professional and show that we are human and that we support our customers. Hope that helps.
Target Market(s)
All small to medium businesses
Industry/Entity Type
Business
Contact Information for Business Card
Martin Forbes
Tall Pine Web Design
17 Wattle Grove Road
West Kelsworth
NSW 2795
0438 527 064
martin@tallpinewebdesign.com.au
www.tallpinewebdesign.com.au

```html
<!DOCTYPE html>
<html lang="en">
<head>
<meta charset="utf-8">
<title>Tall Pine Web Design – Business Card</title>
<link rel="stylesheet" href="https://fonts.googleapis.com/css2?family=Cinzel:wght@400;600&display=swap">
<style>
  :root {
    --page: #e8e5e0;
    --red-deep: #9e0c08;
    --red-mid: #c01a0e;
    --red-warm: #d8321a;
    --band: #dfe2e4;
    --ink-light: #ffffff;
    --ink-soft: #f6dcd6;
    --card-w: 640px;
    --card-h: 366px;
  }
  * { box-sizing: border-box; margin: 0; padding: 0; }
  html, body {
    width: 1200px;
    height: 900px;
    overflow: hidden;
    background: var(--page);
  }
  .canvas {
    width: 1200px;
    height: 900px;
    display: flex;
    flex-direction: column;
    align-items: center;
    justify-content: center;
    gap: 48px;
  }
  .card {
    position: relative;
    width: var(--card-w);
    height: var(--card-h);
    overflow: hidden;
    box-shadow: 0 6px 18px rgba(0, 0, 0, 0.18);
    font-family: "Cinzel", "Times New Roman", serif;
    color: var(--ink-light);
  }
  .card__sky {
    position: absolute;
    inset: 0;
    background:
      linear-gradient(172deg, rgba(255,255,255,0) 0%, rgba(255,90,40,0.10) 38%, rgba(255,255,255,0) 44%, rgba(120,0,0,0.18) 62%, rgba(255,255,255,0) 70%, rgba(230,70,20,0.22) 88%, rgba(255,255,255,0) 100%),
      linear-gradient(180deg, var(--red-deep) 0%, var(--red-mid) 55%, var(--red-warm) 100%);
  }
  /* Front */
  .front__band {
    position: absolute;
    left: 0;
    right: 0;
    top: 56%;
    height: 23%;
    background: var(--band);
  }
  .front__name {
    position: absolute;
    right: 8%;
    top: 40%;
    font-size: 28px;
    font-weight: 400;
    letter-spacing: 2px;
    text-transform: uppercase;
    white-space: nowrap;
  }
  /* Back */
  .back__name {
    position: absolute;
    left: 7%;
    top: 62%;
    font-size: 22px;
    font-weight: 400;
    letter-spacing: 1.5px;
    text-transform: uppercase;
    white-space: nowrap;
  }
  .contact {
    position: absolute;
    left: 53%;
    right: 4%;
    top: 13%;
    text-transform: uppercase;
    font-style: normal;
  }
  .contact__person {
    font-size: 24px;
    font-weight: 400;
    letter-spacing: 1.5px;
    line-height: 1.1;
    white-space: nowrap;
  }
  .contact__company {
    font-size: 13px;
    letter-spacing: 1px;
    margin-bottom: 20px;
    white-space: nowrap;
  }
  .contact__line {
    font-size: 9.5px;
    letter-spacing: 0.6px;
    color: var(--ink-soft);
    margin-bottom: 12px;
    white-space: nowrap;
  }
</style>
</head>
<body>
<main class="canvas">
  <section class="card card--front" aria-label="Card front">
    <div class="card__sky" role="img" aria-label="Streaked red evening sky texture"></div>
    <div class="front__band"></div>
    <h1 class="front__name">Tall Pine Web Design</h1>
  </section>

  <section class="card card--back" aria-label="Card back">
    <div class="card__sky" role="img" aria-label="Streaked red evening sky texture"></div>
    <p class="back__name">Tall Pine Web Design</p>
    <address class="contact">
      <p class="contact__person">Martin Forbes</p>
      <p class="contact__company">Tall Pine Web Design</p>
      <p class="contact__line">17 Wattle Grove Road West Kelsworth NSW 2795</p>
      <p class="contact__line">phone: 0438 527 064</p>
      <p class="contact__line">email: martin@tallpinewebdesign.com.au</p>
      <p class="contact__line">web: www.tallpinewebdesign.com.au</p>
    </address>
  </section>
</main>
</body>
</html>
```